Marketing One-Sheet for Security Deposit Claim Notice

I need a one-sheet flyer formatted for email distribution — optimized as a JPEG/PNG that I can insert into Constant Contact or Outlook. I do not want to attach it to an email, but insert it in the email we send out. I would like it to look professional but engaging. Some images would be good, but want to make sure it reads well if images do not load for the recipients. The text is in the attached Word document, but I am open to changes/ideas that may be better for marketing purposes. I included the URLs for some of the links I would like in the one-sheet that is clickable. The logo for the business is being uploaded on the Word document. Proposed text is also uploaded in a Word document. Thank you.

Target Market(s)

Landlords, Real Estate Agents, Property Managers

Industry/Entity Type

Legal

Requirements
Must have
• Professional but appealing design. The One-sheet is going to be placed in the body of emails, not as an attachment.
Nice to have
• Include our logo for the business and the web links please.
Should not have
• Images can be ok, but it needs to look right if images do not download from the email sent out.

```html
<!DOCTYPE html>
<html lang="en">
<head>
<meta charset="utf-8">
<title>Security Deposit Claim Notice</title>
<link href="https://fonts.googleapis.com/css2?family=Poppins:wght@300;400;500;600;700;800&display=swap" rel="stylesheet">
<style>
:root{
  --red:#e3161f;
  --red-dark:#9c1119;
  --brand:#a51b22;
  --ink:#111111;
  --black:#1a1a1a;
  --white:#ffffff;
  --line:#e9a3a7;
}
*{box-sizing:border-box;margin:0;padding:0}
html,body{width:1200px;height:4839px;overflow:hidden;background:var(--white)}
body{position:relative;font-family:'Poppins',sans-serif;color:var(--ink)}
.abs{position:absolute}
.hero{left:0;top:0;width:1200px;height:958px;background:linear-gradient(180deg,var(--red) 0%,#c41119 50%,var(--red-dark) 100%)}
.brand-box{left:329px;top:0;width:541px;height:400px;background:var(--white);border-radius:0 0 22px 22px;text-align:center;padding-top:66px;color:var(--brand)}
.brand-name{font-weight:600;font-size:56px;line-height:64px;display:flex;align-items:center;justify-content:center;gap:14px}
.brand-name .mark{width:30px;height:30px;background:var(--brand)}
.brand-tag{font-size:19px;line-height:24px;margin-top:14px;font-weight:600}
.brand-contact{font-size:27px;line-height:36px;font-weight:600;margin-top:6px}
.hero-title{left:0;width:1200px;top:498px;text-align:center;color:var(--white);font-weight:800;font-size:84px;line-height:80px;letter-spacing:-2px}
.hero-sub{left:0;width:1200px;top:690px;text-align:center;color:var(--white);font-weight:500;font-size:64px;line-height:80px}
.benefit{top:1117px;width:352px;height:226px;border:2px solid var(--line);border-radius:6px;text-align:center;font-size:38px;line-height:44px;padding-top:50px;color:#222}
.tick{top:1067px;width:84px;height:84px}
.offer-head{left:0;width:1200px;top:1440px;text-align:center;font-size:56px;line-height:62px;font-weight:400;letter-spacing:-1px}
.fee{left:314px;top:1623px;width:572px;height:146px;background:var(--brand);color:var(--white);font-weight:700;font-size:72px;display:flex;align-items:center;justify-content:center}
.law-head{left:83px;top:1884px;width:500px;font-size:50px;line-height:62px;letter-spacing:-1px}
.law-intro{left:83px;top:2030px;width:500px;font-size:41px;line-height:50px;font-weight:300;letter-spacing:-.5px}
.law-list{left:131px;top:2204px;width:430px;list-style:none;font-size:35px;line-height:43px;font-weight:300}
.law-list li{margin-bottom:19px}
.photo{border-radius:10px}
.photo-house{left:620px;top:1884px;width:522px;height:713px;background:linear-gradient(180deg,#9db8d8 0%,#8093a8 45%,#6a9b45 75%,#4f8a2a 100%)}
.photo-tenants{left:56px;top:2693px;width:475px;height:464px;background:linear-gradient(135deg,#e8e3de 0%,#c9b8a6 50%,#5a6a62 100%)}
.warning{left:575px;top:2722px;width:560px;font-size:35px;line-height:42.6px;font-weight:300;letter-spacing:-.6px}
.band{left:0;top:3296px;width:1200px;height:238px;background:var(--black);color:var(--white);text-align:center;font-size:60px;line-height:66px;padding-top:50px;letter-spacing:-1px}
.band strong{font-weight:700}
.btn{display:flex;align-items:center;justify-content:center;color:var(--white);font-size:56px;border-radius:8px;text-decoration:none}
.btn-contact{left:362px;top:3664px;width:476px;height:146px;background:var(--brand)}
.hire{left:0;width:1200px;top:3852px;text-align:center;font-size:52px;line-height:75px;color:var(--brand)}
.hire span{border-bottom:3px solid var(--brand)}
.contact-line{left:0;width:1200px;text-align:center;font-size:52px;line-height:60px;display:flex;justify-content:center;align-items:center;gap:26px}
.btn-more{left:362px;top:4353px;width:476px;height:147px;background:var(--black)}
.btn-docs{left:120px;top:4547px;width:960px;height:146px;background:var(--black)}
</style>
</head>
<body>
<header class="abs hero"></header>
<div class="abs brand-box">
  <div class="brand-name"><span>Tenancy Legal Group</span><span class="mark"></span></div>
  <div class="brand-tag">a Legal Resource for Landlords,<br>Investors &amp; Property Managers</div>
  <div class="brand-contact">TenancyLegalGroup.com<br>1(800) 555-0142</div>
</div>
<h1 class="abs hero-title">SECURITY DEPOSIT<br>CLAIM NOTICE</h1>
<p class="abs hero-sub">Keep the tenant’s<br>Security Deposit</p>

<div class="abs benefit" style="left:53px">Cover<br>unpaid Rent</div>
<div class="abs benefit" style="left:424px">Charge against<br>Damages to<br>the Property</div>
<div class="abs benefit" style="left:796px">Apply to legal<br>fees &amp; costs</div>
<svg class="abs tick" style="left:187px" viewBox="0 0 84 84"><circle cx="42" cy="42" r="41" fill="#a51b22"/><path d="M28 43l10 10 18-20" fill="none" stroke="#fff" stroke-width="4" stroke-linecap="round" stroke-linejoin="round"/></svg>
<svg class="abs tick" style="left:558px" viewBox="0 0 84 84"><circle cx="42" cy="42" r="41" fill="#a51b22"/><path d="M28 43l10 10 18-20" fill="none" stroke="#fff" stroke-width="4" stroke-linecap="round" stroke-linejoin="round"/></svg>
<svg class="abs tick" style="left:930px" viewBox="0 0 84 84"><circle cx="42" cy="42" r="41" fill="#a51b22"/><path d="M28 43l10 10 18-20" fill="none" stroke="#fff" stroke-width="4" stroke-linecap="round" stroke-linejoin="round"/></svg>

<h2 class="abs offer-head">WE PREPARE SECURITY DEPOSIT<br>CLAIM NOTICES</h2>
<div class="abs fee">FLAT FEE $350</div>

<h3 class="abs law-head" style="font-weight:400">Follow Florida law to keep the Deposit</h3>
<p class="abs law-intro">If the Security Deposit Claim is not made correctly &amp; on time, then</p>
<ul class="abs law-list">
  <li>Tenant is automatically entitled to their full deposit back</li>
  <li>No claim against the deposit can be made</li>
  <li>Tenant can sue and recover the deposit and thousands in legal fees</li>
</ul>
<div class="abs photo photo-house" role="img" aria-label="Photo of a two-storey suburban house with a front porch and green lawn"></div>

<div class="abs photo photo-tenants" role="img" aria-label="Photo of a young couple with their dog reviewing a lease at a table"></div>
<p class="abs warning">There are lawyers that specialize in representing tenants and go after landlords that do not make a proper claim against the security deposit. They sue and win their cases &amp; get thousands of dollars in legal fees against Landlords, even if the tenant owes unpaid rent.</p>

<div class="abs band">For commercial properties, the<br><strong>flat legal fee is $450</strong></div>

<a class="abs btn btn-contact" href="#">Contact Us</a>
<p class="abs hire"><span>Hire Us to prepare and serve to</span><br><span>the tenant the security deposit claim</span></p>
<div class="abs contact-line" style="top:4096px">
  <svg width="46" height="46" viewBox="0 0 24 24"><path fill="#e3161f" d="M6.6 10.8a15.1 15.1 0 006.6 6.6l2.2-2.2c.3-.3.7-.4 1-.2 1.1.4 2.3.6 3.6.6.6 0 1 .4 1 1V20c0 .6-.4 1-1 1A17 17 0 013 4c0-.6.4-1 1-1h3.5c.6 0 1 .4 1 1 0 1.3.2 2.5.6 3.6.1.3 0 .7-.2 1z"/></svg>
  <span>1800-555-0142</span>
</div>
<div class="abs contact-line" style="top:4171px">
  <svg width="36" height="46" viewBox="0 0 18 24"><path fill="#e3161f" d="M2 1l14 12-6 .6 3.6 7.4-2.6 1.2-3.5-7.4L2 19z"/></svg>
  <span>TenancyLegalGroup.com</span>
</div>
<a class="abs btn btn-more" href="#">More Info</a>
<a class="abs btn btn-docs" href="#">Request Our Hiring Documents</a>
</body>
</html>
```